Business card design needed

The company name is Pellwick Architects. We are an architectural company based in Melbourne,Australia that has a mix of client base from health care, commercial office, aged care, multi-residential, single residential and retail. Design type is contemporary.

Suggest the base colours need to be black and white. Please leave an area on the back of the card available for handwritten notes.

Target Market(s)

Generally corporate, aged 30 to 65

Industry/Entity Type

Residential

Contact Information for Business Card

Pellwick Architects
Dane Pellwick
7 Horbury Street
Northvale VIC 3059
T (03) 9572 4016
M 0431 607 295
E dp@pellwickarc.com.au

Logo Text

PA

Logo styles of interest
Emblem Logo
Abstract Logo
Lettermark Logo
Requirements
Must have
• I am having trouble attaching a sketch so would really appreciate your effort to try the following brief.

Black and White (B&W)
Would like different card cutout profile. Logo Example, use the half circle curve of the G to form the left edge of the card with no margin. The A is to sit inside the G, connected to the G by its horizontal. The A has its cross bar and lower right leg removed. Card in black, text in white.

Back of card to be black text on white background with services provided.

Client Focused Service
Architecture and Design
Functional Planning
Town Planning
Feasability Studies
Contract Documentation
Contract Administration
Project Management

Simple elegant text, Ariel or similar
Nice to have
• Integrated logo and card cut-out.

Card base black on front, white on back
Should not have
• Too many colours
Fussy details

```html
<!DOCTYPE html>
<html lang="en">
<head>
<meta charset="utf-8">
<title>Pellwick Architects — Business Card</title>
<link href="https://fonts.googleapis.com/css2?family=Arimo:wght@400;700&display=swap" rel="stylesheet">
<style>
  :root {
    --backdrop: #939598;
    --card-front: #3b3a3c;
    --card-back: #ffffff;
    --ink-light: #ffffff;
    --ink-dark: #2b2b2b;
    --divider: #9a9a9a;
  }
  * { margin: 0; padding: 0; box-sizing: border-box; }
  html, body {
    width: 1200px; height: 408px; overflow: hidden;
    background: var(--backdrop);
    font-family: "Arimo", Arial, sans-serif;
  }
  .stage { position: relative; width: 1200px; height: 408px; }
  .card-shapes { position: absolute; inset: 0; }

  .front-rule {
    position: absolute; left: 317px; top: 73px;
    width: 2px; height: 254px; background: var(--ink-light);
  }
  .front-wordmark {
    position: absolute; left: 62px; top: 168px; width: 240px;
    color: var(--ink-light); font-weight: 700; font-size: 26px;
    line-height: 32px; letter-spacing: 1px; text-align: center;
  }
  .front-name {
    position: absolute; left: 333px; top: 132px;
    color: var(--ink-light); font-weight: 700; font-size: 16.5px;
    letter-spacing: 0.2px;
  }
  .front-contact, .front-address {
    position: absolute; right: 649px;
    color: var(--ink-light); font-size: 13.5px; line-height: 18px;
    text-align: right;
  }
  .front-contact { top: 235px; }
  .front-address { top: 301px; }

  .back-services {
    position: absolute; left: 641px; top: 181px; width: 510px;
    color: var(--ink-dark); font-size: 13.5px; line-height: 19.5px;
    text-align: center;
  }
  .service + .service {
    border-left: 1px solid var(--divider);
    padding-left: 3px; margin-left: 1px;
  }
</style>
</head>
<body>
<main class="stage">
  <svg class="card-shapes" width="1200" height="408" viewBox="0 0 1200 408" aria-hidden="true">
    <path class="card-front-shape" d="M190 48 H561 V350 H190 A151 151 0 0 1 190 48 Z" fill="var(--card-front)"/>
    <path class="card-back-shape" d="M641 47 H1016 A150 150 0 0 1 1016 347 H641 Z" fill="var(--card-back)"/>
  </svg>

  <section class="card-front">
    <div class="front-wordmark">PELLWICK<br>ARCHITECTS</div>
    <div class="front-rule"></div>
    <h1 class="front-name">PELLWICK ARCHITECTS</h1>
    <p class="front-contact">
      T (03) 9572 4016<br>
      M 0431 607 295<br>
      E dp@pellwickarc.com.au
    </p>
    <p class="front-address">
      Pellwick Architects Dane Pellwick 7<br>
      Horbury Street Northvale VIC 3059
    </p>
  </section>

  <section class="card-back">
    <p class="back-services">
      <span class="service">Client Focused Service</span><span class="service">Architecture and Design</span><span class="service">Contract Administration</span><br>
      <span class="service">Project Management</span> <span class="service">Town Planning</span><span class="service">Feasability Studies</span><br>
      <span class="service">Contract Documentation</span><span class="service">Functional Planning</span>
    </p>
  </section>
</main>
</body>
</html>
```